Create the artwork for Velvetharbor's debut album, 'Where Rivers Bend Slowly'!

We are a cinematic pop/jazz quartet from Oslo/London looking for someone to create the artwork for our debutalbum, 'Where Rivers Bend Slowly'. This is a project we are incredibly proud of, and we are looking for the perfect artwork to complement our music.

We want the artwork to convey the organic feel of our sound, yet be eye-catching with bright colours. Attached are several examples for inspiration. The title of the album, 'Where Rivers Bend Slowly', should be an inspiration for the design in a subtle/abstract way. Think out of the box here, we are not looking for a hundred solar system designs.

You can find an album teaser here for inspiration: https://audiostreamhub.example/velvetharbormusic/album-teaser

This is our webpage: velvetharbormusic.example

Excited to see what you come up with and to work with some brilliant creatives !

Much love,

Velvetharbor
Updates

Everyone, thanks for your effort and great designs! We're discussing right now and will get back to you with feedback and suggested edits very shortly. Thanks for your patience! Much love, Velvetharbor

Requirements
Must have
• Ready-to-print high-res files in standard CD Cover format
• Artwork ready for digital release on tunewave, Songvault, and social media channels
Nice to have
• Would love to have smaller extensions of the artwork (pattern or pieces of art in same theme) to use on webpage/social media channels.

```html
<!DOCTYPE html>
<html lang="en">
<head>
<meta charset="utf-8">
<title>Where Rivers Bend Slowly</title>
<link rel="stylesheet" href="https://fonts.googleapis.com/css2?family=Pathway+Gothic+One&display=swap">
<style>
  :root {
    --paper: #eef6f7;
    --ink-deep: #04241a;
    --ink-green: #0f6b45;
    --ink-teal: #22b8c4;
    --ink-blue: #2a2fd0;
    --lime: #c6df3a;
    --lime-soft: #dcec86;
    --title-fill: #020d08;
    --title-edge: #ffffff;
  }
  * { margin: 0; padding: 0; box-sizing: border-box; }
  html, body {
    width: 1200px;
    height: 1200px;
    overflow: hidden;
    background: var(--paper);
  }
  .album-cover {
    position: relative;
    width: 1200px;
    height: 1200px;
    overflow: hidden;
  }
  .cover-art {
    position: absolute;
    inset: 0;
    background:
      radial-gradient(ellipse 420px 360px at 820px 280px, var(--ink-deep) 0%, rgba(4,36,26,0.85) 45%, rgba(15,107,69,0) 100%),
      radial-gradient(ellipse 560px 460px at 900px 330px, var(--ink-green) 0%, rgba(15,107,69,0.6) 50%, rgba(15,107,69,0) 100%),
      radial-gradient(ellipse 360px 420px at 1180px 200px, var(--ink-teal) 0%, rgba(34,184,196,0) 100%),
      radial-gradient(ellipse 260px 380px at 1150px 1000px, var(--ink-teal) 0%, rgba(34,184,196,0) 100%),
      radial-gradient(ellipse 170px 120px at 220px 330px, var(--ink-blue) 0%, rgba(42,47,208,0) 100%),
      radial-gradient(ellipse 520px 420px at 460px 960px, var(--lime) 0%, rgba(198,223,58,0.7) 45%, rgba(198,223,58,0) 100%),
      radial-gradient(ellipse 420px 300px at 820px 760px, var(--lime-soft) 0%, rgba(220,236,134,0) 100%),
      linear-gradient(180deg, var(--paper) 0%, #f6fbf6 100%);
  }
  .album-title {
    position: absolute;
    left: 0;
    top: 0;
    width: 1200px;
    height: 1200px;
  }
  .album-title text {
    font-family: "Pathway Gothic One", sans-serif;
    font-size: 210px;
    fill: var(--title-fill);
    stroke: var(--title-edge);
    stroke-width: 5px;
    paint-order: stroke fill;
  }
</style>
</head>
<body>
  <main class="album-cover">
    <div class="cover-art" role="img" aria-label="Dark green, teal and blue ink clouds swirling in water over lime washes, with a blurred grid of letters behind"></div>
    <svg class="album-title" viewBox="0 0 1200 1200" aria-label="Where Rivers Bend Slowly">
      <text x="32" y="912" textLength="1140" lengthAdjust="spacingAndGlyphs">Where Rivers Bend Slowly</text>
    </svg>
  </main>
</body>
</html>
```